Board to put on a meditation centre - Lantern Grove

I need a board design for a new meditation centre based in Oslo which offers free courses in meditation and self-empowerment. The size of the board is width 374cm x height 104cm.  The name of the meditation centre together with subtitles should be on the board but also some elegant decoration that matches the theme (lantern grove/meditation).
Here is the website of the meditation centre to give you a feeling of it: https://lyktelundsenteret.no/
Good if you can use a blue color close to this one: rgb(37, 180, 193) as well as some brown/golden color (similar to the palette on the website).
On the board it should say:
Lyktelunden (in big letters, the rest is subtitles)
Meditasjon & Spirituell visdom
Kurs - Retreat - Dialog
lyktelundsenteret.no
The design should be very elegant and beautiful and the feeling should be of "An Lantern Grove". A logo is here attached and should be used but I need to get a better quality version of it, will upload that as soon as possible.

```html
<!DOCTYPE html>
<html lang="no">
<head>
<meta charset="utf-8">
<title>Lyktelunden – skiltdesign</title>
<link rel="stylesheet" href="https://fonts.googleapis.com/css2?family=Cinzel:wght@400&family=Quicksand:wght@400;500&display=swap">
<style>
  :root {
    --teal: #25aebc;
    --teal-dark: #2a9fab;
    --ink: #111418;
    --white: #ffffff;
    --mist-1: #dcedf5;
    --mist-2: #c3e2e6;
    --mist-3: #a9d9cf;
    --gold-1: #c8962e;
    --gold-2: #e8cf86;
    --gold-3: #b07d22;
    --logo-red: #d6252d;
  }
  * { margin: 0; padding: 0; box-sizing: border-box; }
  html, body { width: 1200px; height: 830px; overflow: hidden; background: var(--white); }
  .canvas { position: relative; width: 1200px; height: 830px; }

  .board {
    position: absolute; left: 88px; width: 1012px; height: 282px;
    background: linear-gradient(110deg, var(--mist-3) 0%, var(--mist-2) 30%, var(--mist-1) 60%, var(--mist-2) 100%);
    overflow: hidden;
  }
  .board--first { top: 72px; }
  .board--second { top: 459px; }

  .board__frame {
    position: absolute; left: 23px; top: 19px; width: 967px; height: 207px;
    background: linear-gradient(120deg, rgba(255,255,255,0.15), rgba(255,255,255,0.45) 50%, rgba(255,255,255,0.2));
    box-shadow: 0 0 3px rgba(90,150,160,0.35);
  }

  .brand {
    position: absolute; left: 60px; top: 99px;
    display: flex; align-items: center; gap: 8px;
    font-family: "Quicksand", sans-serif; font-weight: 500; font-size: 19px;
    color: var(--logo-red);
  }
  .brand__dot { width: 22px; height: 22px; border-radius: 50%; background: var(--logo-red); }

  .title {
    position: absolute; left: 285px; top: 52px;
    font-family: "Cinzel", serif; font-weight: 400; font-size: 76px; line-height: 1;
    color: var(--teal-dark); letter-spacing: 1px; white-space: nowrap;
  }
  .subtitle {
    position: absolute; right: 134px; top: 135px;
    font-family: "Quicksand", sans-serif; font-weight: 500; font-size: 30px; line-height: 1;
    color: var(--ink); white-space: nowrap;
  }

  .web {
    position: absolute; top: 189px; height: 37px;
    background: var(--teal); color: var(--white);
    font-family: "Quicksand", sans-serif; font-weight: 500; font-size: 25px; letter-spacing: 1.5px;
    display: flex; align-items: center; justify-content: center;
  }
  .web--wide { left: 291px; width: 587px; }
  .web--short { left: 451px; width: 427px; }

  .gold-rule {
    position: absolute; left: 0; top: 226px; width: 100%; height: 5px;
    background: linear-gradient(90deg, var(--gold-1), var(--gold-2) 25%, var(--gold-3) 50%, var(--gold-2) 75%, var(--gold-1));
  }
  .nav-band {
    position: absolute; left: 0; top: 231px; width: 100%; height: 51px;
    background: var(--teal);
  }
  .nav-item {
    position: absolute; top: 15px;
    font-family: "Quicksand", sans-serif; font-weight: 400; font-size: 20px; letter-spacing: 12px;
    color: var(--white); line-height: 1;
  }
  .nav-item--kurs { left: 358px; }
  .nav-item--retreat { left: 500px; }
  .nav-item--dialog { left: 713px; }
</style>
</head>
<body>
<div class="canvas">

  <section class="board board--first">
    <div class="board__frame" role="img" aria-label="Soft turquoise marble texture background"></div>
    <div class="brand"><span class="brand__dot"></span>Lyktelunden</div>
    <h1 class="title">LYKTELUNDEN</h1>
    <p class="subtitle">Meditasjon &amp; Spirituell visdom</p>
    <div class="web web--wide">lyktelundsenteret.no</div>
    <div class="gold-rule"></div>
    <nav class="nav-band">
      <span class="nav-item nav-item--kurs">KURS</span>
      <span class="nav-item nav-item--retreat">RETREAT</span>
      <span class="nav-item nav-item--dialog">DIALOG</span>
    </nav>
  </section>

  <section class="board board--second">
    <div class="board__frame" role="img" aria-label="Soft turquoise marble texture background"></div>
    <div class="brand"><span class="brand__dot"></span>Lyktelunden</div>
    <h1 class="title">LYKTELUNDEN</h1>
    <p class="subtitle">Meditasjon &amp; Spirituell visdom</p>
    <div class="web web--short">lyktelundsenteret.no</div>
    <div class="gold-rule"></div>
    <nav class="nav-band">
      <span class="nav-item nav-item--kurs">KURS</span>
      <span class="nav-item nav-item--retreat">RETREAT</span>
      <span class="nav-item nav-item--dialog">DIALOG</span>
    </nav>
  </section>

</div>
</body>
</html>
```